Business card and stationary package

Travel management company looking for designs for single sided business cards, letterhead and envelope. Looking for contemporary designs using our existing logo. Design should clean, not trendy, no gradation of colors and no graphic other than the icon from the logo. Nothing complicated or difficult to read. Should be a crisp design using blue, gray and black colors only.
Letterhead should include a Word template and PDF template.
Business cards are one sided as the reverse will be dynamic images in our company portfolio of images.
We will use the same designer periodically for design projects using the same style guide for upcoming projects as well. Prefer working with designer that will assist with website, brochures and other marketing materials.

Logo Colors and Font:
Blue: 2189c6 Color Hex
Gray: 666666 Color Hex 60% Black
Black: 100% Black
Font: Century Gothic

Target Market(s)

business-to-business

Industry/Entity Type

Travel Industry

Contact Information for Business Card

Sample information for business cards will be:

Daniel Fenwick
Managing Partner

Harborline Journey Services, Inc.
274 Alder Lane, Suite 3621
Westmere, ME 04987

207-555-0148 Direct Dial
207-555-0193 Fax

daniel@harborlinejourney.net
www.harborlinejourney.net

Font styles to use
Sans Serif

Requirements
Must have
• Clean, crisp design, easy to ready, memorable.
Nice to have
• We tend to like dynamic designs that are simple, not trendy, contemporary and easy to read.
Should not have
• no gradation of colors and no graphic other than the icon from the logo, no background images
• **Note that the background should only be white. No black/gary backgrounds or graded colors**

```html
<!DOCTYPE html>
<html lang="en">
<head>
<meta charset="utf-8">
<title>Harborline Journey Services – Business Card</title>
<link href="https://fonts.googleapis.com/css2?family=Didact+Gothic&family=Montserrat:wght@700&display=swap" rel="stylesheet">
<style>
  :root {
    --brand-blue: #2189c6;
    --brand-gray: #666666;
    --brand-black: #000000;
    --tint-blue: #c9dfec;
    --card-white: #ffffff;
    --backdrop: #e9eaec;
  }
  * { box-sizing: border-box; margin: 0; padding: 0; }
  html, body {
    width: 1200px;
    height: 800px;
    overflow: hidden;
    background: var(--backdrop);
  }
  .canvas {
    width: 1200px;
    height: 800px;
    display: flex;
    align-items: center;
    justify-content: center;
  }
  .business-card {
    position: relative;
    width: 1050px;
    height: 600px;
    background: var(--card-white);
    overflow: hidden;
    font-family: "Didact Gothic", "Century Gothic", sans-serif;
    color: var(--brand-gray);
  }
  .accent-circle {
    position: absolute;
    right: -40px;
    top: 40px;
    width: 520px;
    height: 520px;
    border-radius: 50%;
    background: var(--tint-blue);
  }
  .holder {
    position: absolute;
    right: 60px;
    top: 262px;
    width: 380px;
    text-align: center;
  }
  .holder-name {
    font-family: "Montserrat", "Century Gothic", sans-serif;
    font-weight: 700;
    font-size: 26px;
    color: var(--brand-blue);
    text-transform: uppercase;
    line-height: 1.1;
    white-space: nowrap;
  }
  .holder-title {
    margin-top: 10px;
    font-size: 21px;
    color: var(--brand-gray);
  }
  .brand {
    position: absolute;
    left: 80px;
    top: 90px;
    display: flex;
    align-items: center;
    gap: 18px;
  }
  .brand-dot {
    width: 64px;
    height: 64px;
    border-radius: 50%;
    background: var(--brand-blue);
    flex: none;
  }
  .brand-name {
    font-size: 34px;
    letter-spacing: 4px;
    color: var(--brand-gray);
    text-transform: uppercase;
    line-height: 1.05;
  }
  .brand-name span { display: block; font-size: 15px; letter-spacing: 5.4px; margin-top: 6px; }
  .contact-list {
    position: absolute;
    left: 80px;
    top: 290px;
    list-style: none;
  }
  .contact-item {
    display: flex;
    align-items: center;
    gap: 14px;
    font-size: 23px;
    line-height: 34px;
    color: var(--brand-gray);
  }
  .contact-icon { width: 22px; height: 22px; flex: none; }
  .company {
    position: absolute;
    left: 80px;
    top: 445px;
  }
  .company-name {
    font-family: "Montserrat", "Century Gothic", sans-serif;
    font-weight: 700;
    font-size: 21px;
    color: var(--brand-blue);
    margin-bottom: 4px;
  }
  .company-address {
    font-style: normal;
    font-size: 23px;
    line-height: 32px;
    color: var(--brand-gray);
  }
</style>
</head>
<body>
<main class="canvas">
  <article class="business-card">
    <div class="accent-circle"></div>

    <header class="brand">
      <div class="brand-dot"></div>
      <div class="brand-name">Harborline<span>Journey Services</span></div>
    </header>

    <div class="holder">
      <h1 class="holder-name">Daniel Fenwick</h1>
      <p class="holder-title">Managing Partner</p>
    </div>

    <ul class="contact-list">
      <li class="contact-item">
        <svg class="contact-icon" viewBox="0 0 22 22" aria-hidden="true">
          <circle cx="11" cy="11" r="11" fill="var(--brand-blue)"/>
          <path d="M7.5 5.5c.6-.4 1.2-.3 1.6.3l1 1.6c.3.5.2 1.1-.3 1.4l-.7.5c.5 1.2 1.4 2.2 2.6 2.8l.5-.7c.4-.5 1-.6 1.4-.3l1.6 1c.6.4.7 1 .3 1.6-.9 1.3-2.3 1.6-3.9.8-2.3-1.1-4-2.9-5-5.2-.6-1.5-.2-2.7.9-3.6z" fill="#fff"/>
        </svg>
        207-555-0148
      </li>
      <li class="contact-item">
        <svg class="contact-icon" viewBox="0 0 22 22" aria-hidden="true">
          <circle cx="11" cy="11" r="11" fill="var(--brand-blue)"/>
          <rect x="7" y="5" width="8" height="4" fill="#fff"/>
          <rect x="5" y="9.5" width="12" height="5.5" rx="1" fill="#fff"/>
          <rect x="7.5" y="13" width="7" height="4" fill="#fff" stroke="var(--brand-blue)" stroke-width="1"/>
        </svg>
        207-555-0193
      </li>
      <li class="contact-item">
        <svg class="contact-icon" viewBox="0 0 22 22" aria-hidden="true">
          <circle cx="11" cy="11" r="11" fill="var(--brand-blue)"/>
          <rect x="5" y="7" width="12" height="8" fill="#fff"/>
          <path d="M5 7l6 5 6-5" fill="none" stroke="var(--brand-blue)" stroke-width="1.2"/>
        </svg>
        daniel@harborlinejourney.net
      </li>
      <li class="contact-item">
        <svg class="contact-icon" viewBox="0 0 22 22" aria-hidden="true">
          <circle cx="11" cy="11" r="10" fill="none" stroke="var(--brand-blue)" stroke-width="1.6"/>
          <ellipse cx="11" cy="11" rx="4" ry="10" fill="none" stroke="var(--brand-blue)" stroke-width="1.4"/>
          <path d="M1 11h20M3 6h16M3 16h16" stroke="var(--brand-blue)" stroke-width="1.4"/>
        </svg>
        www.harborlinejourney.net
      </li>
    </ul>

    <section class="company">
      <h2 class="company-name">Harborline Journey Services, Inc.</h2>
      <address class="company-address">274 Alder Lane, Suite 3621<br>Westmere, ME 04987</address>
    </section>
  </article>
</main>
</body>
</html>
```